Need new, updated stationery design for an Orthodontic office - to include: Letterhead, Stationery C

Looking for something fresh and sophisticated. We need a stationery design for our new office that is similar to the files attached but do not want it to be exactly what we have now. Needs to include 3 offices - Addresses below:
Harrisburg Office
7315 Orchard Lane, Ste. 214
Harrisburg, NC 28075
Concord Office
2647 Pell-Rose Court NW, Ste. 500
Concord, NC 28025
Charlotte (Fernvale) Office
5913 Fernvale Corporate Parkway, Ste. 409
Charlotte, NC 28277
Phone Number is: 704-318-2967
Office Email: office@marcusweldtorth.example
Dr. Marcus Weldt
Website: www.marcusweldtorth.example
Office

```html
<!DOCTYPE html>
<html lang="en">
<head>
<meta charset="utf-8">
<title>Marcus Weldt Orthodontics — Stationery</title>
<link rel="stylesheet" href="https://fonts.googleapis.com/css2?family=Open+Sans:wght@400;600;700&display=swap">
<style>
  :root{
    --blue:#2b4c96;
    --blue-deep:#22407f;
    --blue-soft:#3a5ba6;
    --ink:#2a2f3a;
    --faint:#e9ecf2;
    --paper:#ffffff;
    --stage:#dcdde0;
    --rule:#9aa3b5;
  }
  *{box-sizing:border-box;margin:0;padding:0}
  html,body{width:1200px;height:2810px;overflow:hidden}
  body{background:var(--stage);font-family:"Open Sans",Arial,sans-serif;color:var(--ink);position:relative}
  .sheet{position:absolute;overflow:hidden;background:var(--paper);box-shadow:0 6px 18px rgba(0,0,0,.18)}

  /* brand lockup */
  .brand{display:flex;align-items:center;gap:10px;font-family:"Open Sans",Arial,sans-serif;font-weight:600;color:var(--blue);line-height:1.05;letter-spacing:.12em;text-transform:uppercase}
  .brand .dot{border-radius:50%;background:currentColor;flex:none}
  .brand.on-blue{color:#fff}

  .faint-circle{position:absolute;border-radius:50%;background:var(--faint)}
  .blue-circle{position:absolute;border-radius:50%;background:var(--blue-soft)}

  /* business card front */
  .card-front{left:40px;top:80px;width:540px;height:309px}
  .card-front .brand{position:absolute;left:26px;top:110px;font-size:17px}
  .card-front .brand .dot{width:34px;height:34px}
  .card-front .details{position:absolute;left:272px;top:26px;font-size:12.5px;line-height:1.35}
  .card-front .doctor{font-size:19px;font-weight:700;color:var(--blue);margin-bottom:4px}
  .card-front .contact{display:flex;align-items:center;gap:6px;color:var(--blue)}
  .card-front .office{margin-top:7px}
  .card-front .office b{color:var(--blue);font-weight:600}
  .card-front .band{position:absolute;left:0;right:0;bottom:0;height:12px;background:var(--blue)}

  /* business card back */
  .card-back{left:620px;top:80px;width:540px;height:309px;background:var(--blue)}
  .card-back .brand{position:absolute;left:150px;top:118px;font-size:20px}
  .card-back .brand .dot{width:40px;height:40px}
  .card-back .web{position:absolute;left:0;right:0;bottom:22px;text-align:center;color:#fff;font-size:12px;letter-spacing:.05em}

  /* envelope front */
  .envelope{left:40px;top:450px;width:540px;height:234px}
  .envelope .brand{position:absolute;left:16px;top:14px;font-size:11px;gap:6px}
  .envelope .brand .dot{width:20px;height:20px}

  /* footer offices */
  .offices{position:absolute;display:flex;border-top:2px solid var(--blue)}
  .offices .col{flex:1;border-left:1px solid var(--rule);padding-left:6px}
  .offices .col:first-child{border-left:none;padding-left:0}
  .offices b{display:block;color:var(--blue);font-weight:700}
  .envelope .offices{left:16px;right:16px;bottom:18px;padding-top:6px;font-size:7px;line-height:1.45}

  /* envelope back */
  .envelope-back{left:620px;top:450px;width:540px;height:234px}
  .envelope-back svg{position:absolute;left:0;top:0}
  .envelope-back .brand{position:absolute;left:205px;top:30px;font-size:12px;gap:6px}
  .envelope-back .brand .dot{width:24px;height:24px}

  /* letterhead */
  .letterhead{left:230px;top:750px;width:740px;height:958px}
  .letterhead .brand{position:absolute;left:40px;top:40px;font-size:22px}
  .letterhead .brand .dot{width:44px;height:44px}
  .letterhead .contact-block{position:absolute;right:30px;top:48px;text-align:right;font-size:11px;line-height:1.6}
  .letterhead .contact-block .doctor{font-size:17px;font-weight:700;color:var(--blue)}
  .letterhead .side-bar{position:absolute;right:0;top:44px;width:10px;height:110px;background:var(--blue)}
  .letterhead .offices{left:40px;right:40px;bottom:40px;padding-top:10px;font-size:11px;line-height:1.55}
  .letterhead .band{position:absolute;left:0;right:0;bottom:0;height:10px;background:var(--blue)}

  /* folder */
  .folder{left:230px;top:1770px;width:740px;height:987px;background:var(--blue)}
  .folder .brand{position:absolute;right:40px;bottom:50px;font-size:24px}
  .folder .brand .dot{width:48px;height:48px}
</style>
</head>
<body>

  <section class="sheet card-front" aria-label="Business card front">
    <div class="brand"><span class="dot"></span><span>Marcus Weldt<br>Orthodontics</span></div>
    <div class="details">
      <div class="doctor">Dr. Marcus Weldt</div>
      <div class="contact">
        <svg width="11" height="11" viewBox="0 0 24 24" aria-hidden="true"><path fill="currentColor" d="M6.6 10.8a15 15 0 0 0 6.6 6.6l2.2-2.2a1 1 0 0 1 1-.25 11 11 0 0 0 3.6.6 1 1 0 0 1 1 1V20a1 1 0 0 1-1 1A17 17 0 0 1 3 4a1 1 0 0 1 1-1h3.5a1 1 0 0 1 1 1 11 11 0 0 0 .6 3.6 1 1 0 0 1-.25 1z"/></svg>
        <span>704-318-2967</span>
      </div>
      <div class="contact">
        <svg width="11" height="11" viewBox="0 0 24 24" aria-hidden="true"><path fill="currentColor" d="M2 5h20v14H2zM4 7v.5l8 5 8-5V7l-8 5z"/></svg>
        <span>office@marcusweldtorth.example</span>
      </div>
      <div class="office"><b>Harrisburg Office</b><br>7315 Orchard Lane, Ste. 214<br>Harrisburg, NC 28075</div>
      <div class="office"><b>Charlotte (Fernvale) Office</b><br>5913 Fernvale Corporate Parkway,<br>Ste. 409 Charlotte, NC 28277</div>
      <div class="office"><b>Concord Office</b><br>2647 Pell-Rose Court NW,<br>Ste. 500 Concord, NC 28025</div>
    </div>
    <div class="band"></div>
  </section>

  <section class="sheet card-back" aria-label="Business card back">
    <div class="blue-circle" style="left:300px;top:-60px;width:360px;height:360px"></div>
    <div class="brand on-blue"><span class="dot"></span><span>Marcus Weldt<br>Orthodontics</span></div>
    <div class="web">www.marcusweldtorth.example</div>
  </section>

  <section class="sheet envelope" aria-label="Envelope front">
    <div class="faint-circle" style="left:180px;top:30px;width:130px;height:130px"></div>
    <div class="brand"><span class="dot"></span><span>Marcus Weldt<br>Orthodontics</span></div>
    <div class="offices">
      <div class="col"><b>Harrisburg Office</b>7315 Orchard Lane, Ste. 214<br>Harrisburg, NC 28075</div>
      <div class="col"><b>Charlotte (Fernvale) Office</b>5913 Fernvale Corporate Parkway, Ste. 409<br>Charlotte, NC 28277</div>
      <div class="col"><b>Concord Office</b>2647 Pell-Rose Court NW, Ste. 500<br>Concord, NC 28025</div>
    </div>
  </section>

  <section class="sheet envelope-back" aria-label="Envelope back">
    <svg width="540" height="234" viewBox="0 0 540 234" aria-hidden="true">
      <path d="M0 0H540V52L270 118L0 52Z" fill="var(--blue)"/>
    </svg>
    <div class="brand on-blue"><span class="dot"></span><span>Marcus Weldt<br>Orthodontics</span></div>
  </section>

  <section class="sheet letterhead" aria-label="Letterhead">
    <div class="brand"><span class="dot"></span><span>Marcus Weldt<br>Orthodontics</span></div>
    <div class="contact-block">
      <div class="doctor">Dr. Marcus Weldt</div>
      <div>Phone Number: 704-318-2967</div>
      <div>Office Email: office@marcusweldtorth.example</div>
      <div>Website: www.marcusweldtorth.example</div>
    </div>
    <div class="side-bar"></div>
    <div class="faint-circle" style="left:290px;top:400px;width:160px;height:160px"></div>
    <div class="offices">
      <div class="col"><b>Harrisburg Office</b>7315 Orchard Lane, Ste. 214<br>Harrisburg, NC 28075</div>
      <div class="col"><b>Charlotte (Fernvale) Office</b>5913 Fernvale Corporate Parkway, Ste. 409<br>Charlotte, NC 28277</div>
      <div class="col"><b>Concord Office</b>2647 Pell-Rose Court NW, Ste. 500<br>Concord, NC 28025</div>
    </div>
    <div class="band"></div>
  </section>

  <section class="sheet folder" aria-label="Presentation folder">
    <div class="blue-circle" style="left:-260px;top:-120px;width:900px;height:900px"></div>
    <div class="brand on-blue"><span class="dot"></span><span>Marcus Weldt<br>Orthodontics</span></div>
  </section>

</body>
</html>
```